Marlowe Consulting Cover 1 - Hunting Funds Like Bibble Hunts the Gronket

Marlowe Consulting is a business consulting firm. We will publish a series of four thought leadership pieces online and via PDF. The first of the series is attached to this project. We need an eye-catching cover page with a back page that keeps with our branding. The document attached is in the final draft, and the cover and pack pages are placeholders only. You can find more about our branding and style on our website www.marloweconsulting.com.au. The other three projects can be found here with a similar brief, and you are welcome to submit a design for all 4.

```html
<!DOCTYPE html>
<html lang="en">
<head>
<meta charset="utf-8">
<title>Marlowe Consulting – Hunting Funds Like Bibble Hunts the Gronket</title>
<link href="https://fonts.googleapis.com/css2?family=Poppins:wght@400;500;600;700&display=swap" rel="stylesheet">
<style>
  :root{
    --stage:#595959;
    --brand-blue:#29a3e0;
    --brand-orange:#f39021;
    --deep-blue:#0a5fa8;
    --mid-blue:#1b8fd6;
    --sky-blue:#3ec0f0;
    --ink:#111111;
    --paper:#ffffff;
    --mist:#e4e6e8;
  }
  *{box-sizing:border-box;margin:0;padding:0}
  html,body{width:844px;height:1200px;overflow:hidden;background:var(--stage)}
  body{font-family:"Poppins",sans-serif;position:relative}
  .page{position:absolute;top:322px;width:400px;height:555px;background:var(--paper);overflow:hidden;box-shadow:0 4px 14px rgba(0,0,0,.35)}
  .page--back{left:18px}
  .page--front{left:426px}
  .page svg.art{position:absolute;inset:0;width:400px;height:555px}

  .brand{position:absolute;display:flex;align-items:center;gap:6px;color:var(--brand-blue);font-weight:600;line-height:1.02}
  .brand__dot{border-radius:50%;background:var(--brand-orange);flex:none}
  .page--front .brand{left:203px;top:40px;font-size:17px}
  .page--front .brand__dot{width:30px;height:30px}
  .page--back .brand{left:28px;top:166px;font-size:10.5px}
  .page--back .brand__dot{width:20px;height:20px}

  .title{position:absolute;left:203px;top:116px;font-size:28px;line-height:31px;color:var(--ink);font-weight:400}
  .title__strong{display:block;font-weight:700;color:var(--brand-blue)}
  .title__line{display:block}
  .title__accent{display:block;font-weight:700;color:var(--brand-orange)}
  .front-url{position:absolute;left:259px;top:492px;font-size:8.6px;color:var(--paper)}

  .pitch{position:absolute;left:28px;top:211px;width:240px;font-size:9.8px;line-height:14.5px;color:var(--ink)}
  .pitch .hl-blue{color:var(--brand-blue)}
  .pitch .hl-orange{color:var(--brand-orange)}

  .contact{position:absolute;left:28px;color:var(--ink)}
  .contact--one{top:313px}
  .contact--two{top:385px}
  .contact__name{font-size:11.5px;font-weight:600;color:var(--brand-blue);line-height:13px}
  .contact__role{font-size:8.8px;color:var(--brand-orange);line-height:11px}
  .contact__row{display:flex;align-items:center;gap:7px;margin-top:6px;font-size:9.6px;line-height:11px}
  .contact__row--mail{margin-top:3px;font-size:7.4px}
  .contact__row svg{width:8px;height:8px;flex:none}

  .follow{position:absolute;left:250px;top:492px;font-size:7.4px;color:var(--ink);display:flex;align-items:center;gap:4px}
  .follow__net{display:inline-block;padding:0 3px;background:var(--ink);color:var(--paper);font-size:6px;line-height:9px;border-radius:1px}
  .back-url{position:absolute;left:250px;top:510px;font-size:8.8px;color:var(--brand-blue)}
</style>
</head>
<body>

<section class="page page--back" aria-label="Back cover">
  <svg class="art" viewBox="0 0 400 555" xmlns="http://www.w3.org/2000/svg">
    <defs>
      <linearGradient id="backCity" x1="0" y1="0" x2="0" y2="1">
        <stop offset="0" stop-color="#f4f5f6"/>
        <stop offset="1" stop-color="#cfd3d6"/>
      </linearGradient>
      <linearGradient id="backTower" x1="0" y1="0" x2="1" y2="1">
        <stop offset="0" stop-color="#123b63"/>
        <stop offset=".45" stop-color="#1f7fc4"/>
        <stop offset="1" stop-color="#2ea7e6"/>
      </linearGradient>
      <linearGradient id="backFade" x1="0" y1="0" x2="0" y2="1">
        <stop offset="0" stop-color="#ffffff" stop-opacity="1"/>
        <stop offset=".55" stop-color="#ffffff" stop-opacity="1"/>
        <stop offset="1" stop-color="#ffffff" stop-opacity="0"/>
      </linearGradient>
      <linearGradient id="prismDark" x1="0" y1="0" x2="1" y2="1">
        <stop offset="0" stop-color="#1d8ad2"/>
        <stop offset="1" stop-color="#0a5fa8"/>
      </linearGradient>
      <linearGradient id="prismLight" x1="0" y1="0" x2="1" y2="1">
        <stop offset="0" stop-color="#1e8fd8"/>
        <stop offset="1" stop-color="#3ec0f0" stop-opacity=".85"/>
      </linearGradient>
      <linearGradient id="edgeGlow" x1="0" y1="0" x2="1" y2="0">
        <stop offset="0" stop-color="#1b8fd6"/>
        <stop offset="1" stop-color="#ffffff"/>
      </linearGradient>
    </defs>
    <rect class="city-photo" width="400" height="555" fill="url(#backCity)" role="img" aria-label="Faded photograph of city skyscrapers seen from below"/>
    <polygon class="tower-photo" points="0,0 400,0 400,180 330,180 0,16" fill="url(#backTower)" role="img" aria-label="Photograph of a glass office tower against blue sky"/>
    <polygon class="white-field" points="0,22 330,186 196,314 0,560" fill="url(#backFade)"/>
    <polygon class="edge-band" points="0,16 330,180 324,186 0,24" fill="url(#edgeGlow)"/>
    <polygon class="prism prism--upper" points="330,180 400,180 400,314 196,314" fill="url(#prismDark)"/>
    <polygon class="prism prism--lower" points="196,314 400,314 400,519" fill="url(#prismLight)"/>
  </svg>

  <div class="brand"><span class="brand__dot"></span><span>Marlowe<br>Consulting</span></div>

  <p class="pitch">Contact us to find out how <span class="hl-blue">Marlowe Consulting</span> can help build your company into a <span class="hl-orange">market leader</span> today.</p>

  <div class="contact contact--one">
    <p class="contact__name">Julian Marlowe</p>
    <p class="contact__role">Managing Director</p>
    <p class="contact__row"><svg viewBox="0 0 10 10"><path d="M2 1l2 2-1 1.2c.6 1.2 1.5 2.1 2.8 2.8L7 6l2 2-1.2 1.2C4.5 9 1 5.5.8 2.2z" fill="#111"/></svg>+61 400 218 346</p>
    <p class="contact__row contact__row--mail"><svg viewBox="0 0 10 10"><rect x=".5" y="2" width="9" height="6" fill="#111"/><path d="M.5 2l4.5 3.5L9.5 2" stroke="#fff" stroke-width=".8" fill="none"/></svg>julian@marloweconsulting.com.au</p>
  </div>

  <div class="contact contact--two">
    <p class="contact__name">Simon Marlowe</p>
    <p class="contact__role">Managing Director</p>
    <p class="contact__row"><svg viewBox="0 0 10 10"><path d="M2 1l2 2-1 1.2c.6 1.2 1.5 2.1 2.8 2.8L7 6l2 2-1.2 1.2C4.5 9 1 5.5.8 2.2z" fill="#111"/></svg>+61 400 573 901</p>
    <p class="contact__row contact__row--mail"><svg viewBox="0 0 10 10"><rect x=".5" y="2" width="9" height="6" fill="#111"/><path d="M.5 2l4.5 3.5L9.5 2" stroke="#fff" stroke-width=".8" fill="none"/></svg>simon@marloweconsulting.com.au</p>
  </div>

  <p class="follow">Follow us: <span class="follow__net">Netlink</span><span class="follow__net">Chirp</span></p>
  <p class="back-url">marloweconsulting.com.au</p>
</section>

<section class="page page--front" aria-label="Front cover">
  <svg class="art" viewBox="0 0 400 555" xmlns="http://www.w3.org/2000/svg">
    <defs>
      <linearGradient id="frontCity" x1="0" y1="0" x2="0" y2="1">
        <stop offset="0" stop-color="#ffffff"/>
        <stop offset=".5" stop-color="#f2f4f6"/>
        <stop offset="1" stop-color="#d6dadd"/>
      </linearGradient>
      <linearGradient id="frontTower" x1="0" y1="0" x2="1" y2="1">
        <stop offset="0" stop-color="#2aa2df"/>
        <stop offset=".6" stop-color="#1a6fb0"/>
        <stop offset="1" stop-color="#123e68"/>
      </linearGradient>
      <linearGradient id="frontPrism" x1="0" y1="0" x2="1" y2="1">
        <stop offset="0" stop-color="#1779c2"/>
        <stop offset="1" stop-color="#0a5fa8"/>
      </linearGradient>
      <linearGradient id="frontBlock" x1="1" y1="0" x2="0" y2="1">
        <stop offset="0" stop-color="#1b8fd6"/>
        <stop offset=".5" stop-color="#1464a8"/>
        <stop offset="1" stop-color="#2aa0dd"/>
      </linearGradient>
      <linearGradient id="frontHaze" x1="0" y1="0" x2="1" y2="1">
        <stop offset="0" stop-color="#3ec0f0" stop-opacity=".8"/>
        <stop offset="1" stop-color="#ffffff" stop-opacity="0"/>
      </linearGradient>
    </defs>
    <rect class="city-photo" width="400" height="555" fill="url(#frontCity)" role="img" aria-label="Faded photograph of city skyscrapers in light haze"/>
    <rect class="tower-photo" x="0" y="0" width="177" height="314" fill="url(#frontTower)" role="img" aria-label="Photograph of a glass office tower reflecting the sky"/>
    <rect class="edge-band" x="177" y="0" width="12" height="314" fill="#1b8fd6"/>
    <polygon class="prism" points="0,200 177,314 0,314" fill="url(#frontPrism)"/>
    <polygon class="haze" points="0,314 177,314 120,430 0,400" fill="url(#frontHaze)"/>
    <polygon class="edge-band" points="400,220 400,232 72,555 62,555" fill="#29a3e0"/>
    <polygon class="block-photo" points="400,232 400,555 72,555" fill="url(#frontBlock)" role="img" aria-label="Photograph of blue glass high-rise buildings"/>
  </svg>

  <div class="brand"><span class="brand__dot"></span><span>Marlowe<br>Consulting</span></div>

  <h1 class="title">
    <span class="title__strong">Hunting</span>
    <span class="title__strong">Funds</span>
    <span class="title__line">Like Bibble</span>
    <span class="title__line">Hunts the</span>
    <span class="title__accent">Gronket</span>
  </h1>

  <p class="front-url">marloweconsulting.com.au</p>
</section>

</body>
</html>
```